Marvane Painting Epoxy Flyer

We need a promotional flyer for a new epoxy floor coatings division of our painting company. We do epoxy garage floor coatings and paver sealing. It needs to be based on and very similar to the attached flyer. The garage floor picture needs to look more realistic, and the before and after pavers pictures should look less shiny but still a good contrast. Include attached logo

```html
<!DOCTYPE html>
<html lang="en">
<head>
<meta charset="utf-8">
<title>Marvane Painting – Epoxy Flyer</title>
<link href="https://fonts.googleapis.com/css2?family=Oswald:wght@500;600&family=Barlow+Semi+Condensed:ital,wght@0,400;0,500;1,400&family=Allura&family=Playfair+Display:ital,wght@1,600&family=Roboto:wght@700;900&display=swap" rel="stylesheet">
<style>
  :root{
    --blue:#0b3f98;
    --green:#3e8f0a;
    --green-bright:#4cb81a;
    --panel:#ececec;
    --ink:#1c1c1c;
    --text:#2a2a2a;
    --white:#ffffff;
  }
  *{box-sizing:border-box;margin:0;padding:0}
  html,body{width:970px;height:1200px;overflow:hidden;background:#fff}
  .flyer{position:relative;width:970px;height:1200px;overflow:hidden;
    background:linear-gradient(160deg,#fafafa 0%,#ffffff 45%,#f4f4f4 100%);
    font-family:"Barlow Semi Condensed",sans-serif;color:var(--text)}
  .abs{position:absolute}

  .brand{left:40px;top:110px;width:330px;display:flex;align-items:center;gap:14px}
  .brand-dot{width:46px;height:46px;border-radius:50%;background:var(--blue);flex:none}
  .brand-name{font-family:"Oswald",sans-serif;font-weight:600;font-size:36px;color:var(--ink);letter-spacing:.5px;white-space:nowrap}

  .rule-green{left:0;top:292px;width:390px;height:6px;background:var(--green-bright)}
  .hero-band{left:0;top:301px;width:970px;height:232px;background:var(--blue)}

  .photo-frame{left:392px;top:19px;width:564px;height:383px;background:var(--white)}
  .photo{position:absolute}
  .photo svg{display:block;width:100%;height:100%}
  .garage{left:8px;top:8px;width:359px;height:368px}
  .pavers-before{left:371px;top:8px;width:184px;height:184px;background:linear-gradient(150deg,#6f665c,#5d564e 60%,#4f4a44)}
  .pavers-after{left:371px;top:196px;width:184px;height:180px;background:linear-gradient(150deg,#8a6a52,#7a5a44 60%,#6a4e3b)}

  .tag{position:absolute;font-family:"Roboto",sans-serif;font-weight:700;font-size:15px;color:#fff;
    padding:3px 12px;letter-spacing:.3px;clip-path:polygon(6% 0,100% 0,94% 100%,0 100%)}
  .tag.before{background:var(--blue)}
  .tag.after{background:var(--green)}

  .script{left:50px;top:318px;font-family:"Allura",cursive;font-size:104px;color:var(--green-bright);line-height:1}
  .headline{left:61px;top:430px;font-family:"Oswald",sans-serif;font-weight:600;font-size:62px;color:#fff;line-height:1;letter-spacing:.3px}
  .subline{left:715px;top:440px;font-family:"Playfair Display",serif;font-style:italic;font-weight:600;font-size:25px;color:var(--green-bright);line-height:1.12}

  .services{left:57px;top:573px;width:855px;height:200px;display:flex;gap:10px}
  .service{flex:1;background:var(--panel)}
  .service-head{height:50px;display:flex;align-items:center;justify-content:center;
    font-family:"Oswald",sans-serif;font-weight:500;font-size:28px;color:#fff;letter-spacing:.2px}
  .service.epoxy .service-head{background:var(--blue);clip-path:polygon(0 0,100% 0,97.5% 100%,0 100%);padding-right:14px}
  .service.paver .service-head{background:var(--green);clip-path:polygon(1.5% 0,100% 0,100% 100%,0 100%)}
  .ticks{list-style:none;padding-top:16px}
  .service.epoxy .ticks{padding-left:66px}
  .service.paver .ticks{padding-left:52px}
  .ticks li{display:flex;align-items:center;gap:6px;font-size:20px;height:29px;color:var(--text)}
  .ticks svg{width:17px;height:17px;flex:none}

  .values{left:57px;top:794px;width:855px;height:189px;background:var(--panel)}
  .values-head{height:50px;background:var(--blue);display:flex;align-items:center;justify-content:center;
    font-family:"Oswald",sans-serif;font-weight:500;font-size:29px;color:#fff;letter-spacing:.2px}
  .value{position:absolute;top:71px;display:flex;align-items:center;gap:20px}
  .value-icon{width:86px;height:86px;border-radius:50%;display:flex;align-items:center;justify-content:center;
    box-shadow:0 0 0 2px #fff,0 0 0 3px var(--green)}
  .value-icon.blue{background:var(--blue)}
  .value-icon.green{background:var(--green);box-shadow:0 0 0 2px #fff,0 0 0 3px var(--blue)}
  .value-icon svg{width:50px;height:50px}
  .value-text{font-size:22px;line-height:1.25;color:var(--text)}

  .cta{left:0;top:1010px;width:970px;text-align:center}
  .cta-title{font-family:"Oswald",sans-serif;font-weight:500;font-size:38px;color:var(--blue);display:flex;justify-content:center;align-items:center;gap:12px}
  .cta-title::before,.cta-title::after{content:"";width:36px;height:3px;background:var(--blue)}
  .cta-phone{display:flex;justify-content:center;align-items:center;gap:10px;margin-top:-4px}
  .cta-phone svg{width:56px;height:56px}
  .phone-number{font-family:"Roboto",sans-serif;font-weight:900;font-size:70px;color:#111;letter-spacing:1px;line-height:1.05}
  .cta-tagline{font-style:italic;font-size:24px;color:var(--green);margin-top:2px}

  .foot-bar{top:1187px;height:13px}
  .foot-bar.left{left:0;width:221px;background:var(--blue)}
  .foot-bar.mid{left:235px;width:498px;background:var(--green)}
  .foot-bar.right{left:747px;width:223px;background:var(--blue)}
</style>
</head>
<body>
<div class="flyer">

  <div class="abs brand">
    <span class="brand-dot"></span>
    <span class="brand-name">MARVANE PAINTING</span>
  </div>

  <div class="abs rule-green"></div>
  <div class="abs hero-band"></div>

  <div class="abs photo-frame">
    <div class="photo garage" role="img" aria-label="Garage floor before and after: bare stained concrete on the left, grey flake epoxy coating on the right">
      <svg viewBox="0 0 359 368" preserveAspectRatio="none">
        <defs>
          <linearGradient id="concrete" x1="0" y1="0" x2="1" y2="1">
            <stop offset="0" stop-color="#8d877c"/><stop offset=".5" stop-color="#6f6a62"/><stop offset="1" stop-color="#5c5852"/>
          </linearGradient>
          <linearGradient id="epoxy" x1="0" y1="0" x2="0" y2="1">
            <stop offset="0" stop-color="#c9c9c9"/><stop offset=".2" stop-color="#8e9297"/><stop offset="1" stop-color="#6e7277"/>
          </linearGradient>
        </defs>
        <polygon points="0,0 222,0 165,368 0,368" fill="url(#concrete)"/>
        <polygon points="222,0 359,0 359,368 165,368" fill="url(#epoxy)"/>
        <line x1="222" y1="0" x2="165" y2="368" stroke="#fff" stroke-width="4"/>
      </svg>
      <span class="tag before" style="left:113px;top:177px">BEFORE</span>
      <span class="tag after" style="left:196px;top:177px">AFTER</span>
    </div>
    <div class="photo pavers-before" role="img" aria-label="Faded grey brick pavers beside a wooden fence before sealing">
      <span class="tag before" style="left:0;top:160px">BEFORE</span>
    </div>
    <div class="photo pavers-after" role="img" aria-label="Warm reddish brick pavers beside a wooden fence after sealing">
      <span class="tag after" style="right:0;bottom:0">AFTER</span>
    </div>
  </div>

  <div class="abs script">Upgarde</div>
  <div class="abs headline">Your Garage &amp; Driveway</div>
  <div class="abs subline">From worn-out<br>to like new</div>

  <div class="abs services">
    <section class="service epoxy">
      <h2 class="service-head">EPROXY FLOOR COATINGS</h2>
      <ul class="ticks">
        <li><svg viewBox="0 0 20 20"><circle cx="10" cy="10" r="8.5" fill="none" stroke="#0b3f98" stroke-width="1.8"/><path d="M6 10.5l3 3 5.5-6" fill="none" stroke="#0b3f98" stroke-width="1.8"/></svg>Durable, long-lasting finish</li>
        <li><svg viewBox="0 0 20 20"><circle cx="10" cy="10" r="8.5" fill="none" stroke="#0b3f98" stroke-width="1.8"/><path d="M6 10.5l3 3 5.5-6" fill="none" stroke="#0b3f98" stroke-width="1.8"/></svg>Slip-resistant texture</li>
        <li><svg viewBox="0 0 20 20"><circle cx="10" cy="10" r="8.5" fill="none" stroke="#0b3f98" stroke-width="1.8"/><path d="M6 10.5l3 3 5.5-6" fill="none" stroke="#0b3f98" stroke-width="1.8"/></svg>Covers cracks &amp; imperfections</li>
        <li><svg viewBox="0 0 20 20"><circle cx="10" cy="10" r="8.5" fill="none" stroke="#0b3f98" stroke-width="1.8"/><path d="M6 10.5l3 3 5.5-6" fill="none" stroke="#0b3f98" stroke-width="1.8"/></svg>Easy to clean &amp; maintain</li>
      </ul>
    </section>
    <section class="service paver">
      <h2 class="service-head">PAVER SEALING</h2>
      <ul class="ticks">
        <li><svg viewBox="0 0 20 20"><circle cx="10" cy="10" r="8.5" fill="none" stroke="#3e8f0a" stroke-width="1.8"/><path d="M6 10.5l3 3 5.5-6" fill="none" stroke="#3e8f0a" stroke-width="1.8"/></svg>Restores color &amp; enhances appearance</li>
        <li><svg viewBox="0 0 20 20"><circle cx="10" cy="10" r="8.5" fill="none" stroke="#3e8f0a" stroke-width="1.8"/><path d="M6 10.5l3 3 5.5-6" fill="none" stroke="#3e8f0a" stroke-width="1.8"/></svg>Protects from sun fading</li>
        <li><svg viewBox="0 0 20 20"><circle cx="10" cy="10" r="8.5" fill="none" stroke="#3e8f0a" stroke-width="1.8"/><path d="M6 10.5l3 3 5.5-6" fill="none" stroke="#3e8f0a" stroke-width="1.8"/></svg>Helps prevent weeds &amp; sand loss</li>
        <li><svg viewBox="0 0 20 20"><circle cx="10" cy="10" r="8.5" fill="none" stroke="#3e8f0a" stroke-width="1.8"/><path d="M6 10.5l3 3 5.5-6" fill="none" stroke="#3e8f0a" stroke-width="1.8"/></svg>Easier to clean &amp; maintain</li>
      </ul>
    </section>
  </div>

  <div class="abs values">
    <h2 class="values-head">PRACTICAL UPGARDES THAT PROTECT AND IMPROVE YOUR HOME</h2>
    <div class="value" style="left:50px">
      <div class="value-icon blue">
        <svg viewBox="0 0 50 50" fill="none" stroke="#fff" stroke-width="2.2" stroke-linejoin="round"><path d="M25 5l16 6v12c0 11-7 18-16 22C16 41 9 34 9 23V11z"/><path d="M17 25l6 6 11-12"/></svg>
      </div>
      <div class="value-text">Licensed &amp;<br>Insured</div>
    </div>
    <div class="value" style="left:285px">
      <div class="value-icon green">
        <svg viewBox="0 0 50 50" fill="none" stroke="#fff" stroke-width="2.2" stroke-linecap="round"><path d="M12 12l26 26"/><path d="M9 9l5-2 3 3-2 5-3-1z"/><path d="M38 12l-24 24"/><circle cx="12" cy="38" r="4"/><path d="M34 9a6 6 0 0 0 7 7"/></svg>
      </div>
      <div class="value-text">Family-Owned<br>Local Business</div>
    </div>
    <div class="value" style="left:545px">
      <div class="value-icon blue">
        <svg viewBox="0 0 50 50" fill="none" stroke="#fff" stroke-width="2.2" stroke-linejoin="round"><path d="M25 33c-6-8-9-12-9-17a9 9 0 0 1 18 0c0 5-3 9-9 17z"/><circle cx="25" cy="16" r="3.5"/><path d="M14 32l-6 10h34l-6-10"/></svg>
      </div>
      <div class="value-text">Serving Prescott &amp;<br>Surrounding Areas</div>
    </div>
  </div>

  <div class="abs cta">
    <div class="cta-title">CALL FOR A FREE EXTIMATE</div>
    <div class="cta-phone">
      <svg viewBox="0 0 56 56" fill="none" stroke="#3e8f0a" stroke-width="2.6" stroke-linejoin="round" stroke-linecap="round"><path d="M14 8l7 11-4 5c3 6 8 11 14 14l5-4 11 7-4 8C27 50 6 29 6 12z"/><path d="M32 10a16 16 0 0 1 14 14"/><path d="M32 17a9 9 0 0 1 7 7"/></svg>
      <span class="phone-number">928-555-0147</span>
    </div>
    <div class="cta-tagline">Fast, professional service you can trust</div>
  </div>

  <div class="abs foot-bar left"></div>
  <div class="abs foot-bar mid"></div>
  <div class="abs foot-bar right"></div>
</div>
</body>
</html>
```